Locksmith business card design

i need a business card design for a new locksmith/auto Locksmith company we cater for residental/commercial/industrial/vehicles locksmithing we provide a 24/7 emergency service we are fully insured and certified i like the idea of black with white writing i would like the final design to communicate we are very affordable compared to our competitors

Target Market(s)

everyone

Industry/Entity Type

Business

Contact Information for Business Card

Bramwell's 24h Locksmiths, Owen Bramwell, 27 fenwick lane ashcombe vale so482kt, bramwells_locksmiths@quillmail.com,07841296035,www.bramwellslocksmith.com

Requirements
Must have
• some sort of logo/picture

```html
<!DOCTYPE html>
<html lang="en">
<head>
<meta charset="utf-8">
<title>Bramwell's 24h Locksmiths – Business Card</title>
<link rel="stylesheet" href="https://fonts.googleapis.com/css2?family=Gelasio:wght@400&display=swap">
<style>
  :root {
    --page-bg: #efe5dc;
    --card-bg: #161412;
    --ink: #ffffff;
    --key-silver-light: #d9d9d9;
    --key-silver-dark: #6f6f6f;
  }
  * { margin: 0; padding: 0; box-sizing: border-box; }
  html, body {
    width: 1200px;
    height: 1085px;
    overflow: hidden;
    background: var(--page-bg);
  }
  body {
    position: relative;
    font-family: "Gelasio", Georgia, serif;
    color: var(--ink);
  }
  .card {
    position: absolute;
    width: 640px;
    height: 402px;
    background: var(--card-bg);
  }
  .card--front { left: 116px; top: 90px; }
  .card--back  { left: 436px; top: 596px; }

  .key-art {
    position: absolute;
    border-radius: 10px;
    background: radial-gradient(circle at 40% 35%, var(--key-silver-light), var(--key-silver-dark) 70%, var(--card-bg) 100%);
    opacity: 0.85;
  }
  .card--front .key-art { left: 26px; top: 78px; width: 180px; height: 252px; }
  .card--back  .key-art { left: 431px; top: 22px; width: 189px; height: 180px; }

  .divider {
    position: absolute;
    background: var(--ink);
  }
  .card--front .divider { left: 226px; top: 26px; width: 4px; height: 352px; }
  .card--back  .divider { left: 20px; top: 168px; width: 5px; height: 192px; }

  .front-title {
    position: absolute;
    left: 236px;
    width: 404px;
    top: 72px;
    text-align: center;
    font-size: 70px;
    line-height: 72px;
    font-weight: 400;
  }

  .back-title {
    position: absolute;
    font-size: 36px;
    font-weight: 400;
    line-height: 1;
    white-space: nowrap;
  }
  .back-title__top { left: 36px; top: 45px; }
  .back-title__bottom { left: 252px; top: 86px; }

  .owner {
    position: absolute;
    left: 36px;
    top: 172px;
    font-size: 31px;
    line-height: 1;
    white-space: nowrap;
  }
  .contact-list {
    position: absolute;
    left: 36px;
    top: 246px;
    list-style: none;
    font-size: 22px;
    line-height: 31px;
    white-space: nowrap;
  }
</style>
</head>
<body>
  <section class="card card--front">
    <div class="key-art" role="img" aria-label="Silver key in a lock with a pound-sign key fob"></div>
    <div class="divider"></div>
    <h1 class="front-title">Bramwell's<br>24h<br>Locksmiths</h1>
  </section>

  <section class="card card--back">
    <div class="back-title back-title__top">Bramwell's 24h</div>
    <div class="back-title back-title__bottom">Locksmiths</div>
    <div class="key-art" role="img" aria-label="Silver key in a lock with a pound-sign key fob"></div>
    <div class="divider"></div>
    <p class="owner">Owen Bramwell - Owner</p>
    <ul class="contact-list">
      <li>Address : 27 Fenwick Lane,Ashcombe Vale so482kt</li>
      <li>Email : bramwells_locksmiths@quillmail.com</li>
      <li>Phone : 07841296035</li>
      <li>Web : www.bramwellslocksmith.com</li>
    </ul>
  </section>
</body>
</html>
```